Flyer to University MBA Directors about my new online course

I have a new online course call Advisory Summit which helps graduates land jobs in top consultancies. I will be selling it to MBA Directors and Employability Managers in Universities. I would like a flyer that (a) sells my online course (b) introduces me (c) sells my workshops.
Updates

I don't mind if this is A4 or A5, or one or two sided, landscape or portrait. Could you please add my email to the flyer (max@advisorysummit.example)? Feel free to edit the text if it doesn't fit (e.g. replacing 'and' with &) etc.

Target Market(s)

MBA Directors & Employability Managers at Universities

Industry/Entity Type

Education

Font styles to use
Serif

Colors

Designer to choose colors to be used in the design.

Requirements
Must have
• Please add my email (max@advisorysummit.example).
• Please have one of the logos attached.
• Please add the text (or similar) in the attached.
• Please see my website (www.advisorysummit.example) for an idea of look & feel
Nice to have
• Please use a cityscape skyline as a background to one of my photos
• Please use a 2x2 matrix with icons for the 'what you get' section
• Please put the section about workshops & testimonials on the reverse
• Please use dark colours (see my website www.advisorysummit.example)

```html
<!DOCTYPE html>
<html lang="en">
<head>
<meta charset="utf-8">
<title>Advisory Summit – Flyer</title>
<link href="https://fonts.googleapis.com/css2?family=Libre+Baskerville:wght@700&family=Mulish:wght@700;800&family=Questrial&display=swap" rel="stylesheet">
<style>
  :root{
    --stage:#9b9b9b;
    --paper:#ffffff;
    --ink-text:#333333;
    --blue:#1f86cf;
    --blue-light:#2aa3e6;
    --blue-deep:#176fb6;
    --tab-dark:#2c2c2c;
    --tab-mid:#4a4a4a;
    --footer:#333333;
    --white:#ffffff;
  }
  *{box-sizing:border-box;margin:0;padding:0}
  html,body{width:1200px;height:1200px;overflow:hidden;background:var(--stage)}
  body{position:relative;font-family:"Questrial",sans-serif}
  .flyer{position:absolute;left:180px;top:10px;width:841px;height:1180px;background:var(--paper);overflow:hidden}
  .header-shape{position:absolute;left:0;top:0;width:841px;height:305px}
  .brand{position:absolute;left:620px;top:24px;width:216px;text-align:center}
  .brand-dot{width:70px;height:70px;border-radius:50%;background:var(--blue);margin:0 auto 12px}
  .brand-name{font-family:"Libre Baskerville",serif;font-weight:700;color:var(--blue);font-size:18px;line-height:22px;letter-spacing:.6px;white-space:nowrap}
  .headline{position:absolute;left:35px;top:82px;font-family:"Libre Baskerville",serif;font-weight:700;color:var(--white);font-size:34px;line-height:41px;letter-spacing:.2px}
  .header-url{position:absolute;left:35px;top:215px;color:var(--blue-light);font-size:25px;letter-spacing:.4px}
  .highlights{position:absolute;left:0;top:303px;width:841px;height:82px;background:linear-gradient(90deg,var(--blue-deep),var(--blue) 50%,var(--blue-deep))}
  .highlights-notch{position:absolute;left:405px;top:-14px;width:0;height:0;border-left:16px solid transparent;border-right:16px solid transparent;border-bottom:14px solid var(--blue)}
  .highlight{position:absolute;top:12px;display:flex;align-items:center;gap:15px;color:var(--white);font-size:14.5px;line-height:17px}
  .highlight-icon{width:58px;height:58px;border-radius:50%;background:var(--white);display:flex;align-items:center;justify-content:center;flex:none}
  .tab{position:absolute;left:0;height:32px;border-radius:0 16px 16px 0;background:linear-gradient(180deg,var(--tab-mid),var(--tab-dark));color:var(--white);font-family:"Mulish",sans-serif;font-weight:800;font-size:18px;line-height:32px;box-shadow:0 8px 10px -4px rgba(0,0,0,.35)}
  .list{position:absolute;list-style:none;font-size:14px}
  .list li{display:flex;align-items:flex-start;gap:8px}
  .list svg{flex:none;margin-top:2px}
  .get-list{color:var(--ink-text);line-height:17px}
  .get-list li{margin-bottom:3px}
  .get-list li span{text-align:justify}
  .advice{position:absolute;left:0;top:551px;width:841px;height:222px;background:linear-gradient(90deg,var(--blue-deep),var(--blue-light) 45%,var(--blue) 100%)}
  .advice-list{color:var(--white);line-height:19.2px}
  .portrait{position:absolute;left:583px;top:683px;width:258px;height:440px}
  .bio{position:absolute;left:42px;top:849px;width:548px;font-size:14.2px;line-height:16.5px;color:var(--ink-text);text-align:justify}
  .price{position:absolute;top:1019px;width:94px;height:94px;margin-left:-47px;border-radius:50%;background:linear-gradient(180deg,var(--blue-light),var(--blue-deep));color:var(--white);text-align:center}
  .price-label{position:absolute;left:0;right:0;font-size:12px;line-height:14px}
  .price-ribbon{position:absolute;left:-14px;top:41px;width:122px;height:24px;background:var(--tab-dark);clip-path:polygon(0 0,100% 0,94% 50%,100% 100%,0 100%,6% 50%);font-family:"Mulish",sans-serif;font-weight:800;font-size:19px;line-height:24px}
  .footer{position:absolute;left:0;top:1123px;width:841px;height:57px;background:linear-gradient(90deg,#2a2a2a,var(--footer) 50%,#2a2a2a);color:var(--white);text-align:center;font-size:17px;line-height:50px;letter-spacing:1.6px;white-space:nowrap}
  .footer-sep{margin:0 14px;color:var(--blue-light)}
</style>
</head>
<body>
<main class="flyer">
  <svg class="header-shape" viewBox="0 0 841 305" aria-hidden="true">
    <defs>
      <linearGradient id="headerFill" x1="0" y1="0" x2="1" y2="1">
        <stop offset="0" stop-color="#262626"/>
        <stop offset="1" stop-color="#1a1d1c"/>
      </linearGradient>
    </defs>
    <path d="M0 20 H540 Q568 20 582 44 L618 140 Q628 161 660 161 H841 V305 H0 Z" fill="url(#headerFill)"/>
  </svg>

  <div class="brand">
    <div class="brand-dot"></div>
    <div class="brand-name">ADVISORY SUMMIT</div>
  </div>

  <h1 class="headline">BOOST YOUR GRADUATES’<br>EMPLOYABILITY AND<br>STARTING SALARIES WITH</h1>
  <div class="header-url">www.AdvisorySummit.example</div>

  <section class="highlights">
    <span class="highlights-notch"></span>
    <div class="highlight" style="left:39px">
      <span class="highlight-icon">
        <svg width="36" height="30" viewBox="0 0 36 30"><path d="M18 3 L35 11 L18 19 L1 11 Z" fill="#222"/><path d="M8 15 V23 Q18 29 28 23 V15 L18 20 Z" fill="#222"/><path d="M32 12 V22" stroke="#222" stroke-width="2"/><circle cx="32" cy="23" r="2" fill="#222"/></svg>
      </span>
      <span>#1 career<br>choice for graduates</span>
    </div>
    <div class="highlight" style="left:306px">
      <span class="highlight-icon">
        <svg width="32" height="36" viewBox="0 0 32 36"><circle cx="16" cy="10" r="8" fill="#222"/><path d="M2 36 Q2 21 16 21 Q30 21 30 36 Z" fill="#222"/><path d="M16 22 L14 27 L16 34 L18 27 Z" fill="#fff"/></svg>
      </span>
      <span>Biggest employer<br>of top graduates</span>
    </div>
    <div class="highlight" style="left:564px">
      <span class="highlight-icon">
        <svg width="36" height="36" viewBox="0 0 36 36" fill="none" stroke="#222" stroke-width="2.4"><circle cx="22" cy="12" r="9"/><path d="M22 7 V17 M19 10 H24 M19 14 H25"/><path d="M3 22 H9 V34 H3 Z M9 24 H17 Q20 24 20 27 H12 M9 32 H22 L31 25"/></svg>
      </span>
      <span>Highest starting<br>salaries outside banking</span>
    </div>
  </section>

  <h2 class="tab" style="top:410px;width:175px;padding-left:9px">WHAT YOU GET:</h2>
  <ul class="list get-list" style="left:41px;top:460px;width:310px">
    <li><svg width="13" height="13" viewBox="0 0 13 13"><circle cx="6.5" cy="6.5" r="5.2" fill="none" stroke="#1f86cf" stroke-width="1.6"/><path d="M3.8 6.5 L6 8.8 L12 2.5" fill="none" stroke="#1f86cf" stroke-width="1.8"/></svg><span>50 ‘bite-sized’ videos on all aspects of the consulting recruitment process</span></li>
    <li><svg width="13" height="13" viewBox="0 0 13 13"><circle cx="6.5" cy="6.5" r="5.2" fill="none" stroke="#1f86cf" stroke-width="1.6"/><path d="M3.8 6.5 L6 8.8 L12 2.5" fill="none" stroke="#1f86cf" stroke-width="1.8"/></svg><span>15 downloadable templates, cheat-sheets and score-cards</span></li>
  </ul>
  <ul class="list get-list" style="left:494px;top:460px;width:320px">
    <li style="margin-bottom:16px"><svg width="13" height="13" viewBox="0 0 13 13"><circle cx="6.5" cy="6.5" r="5.2" fill="none" stroke="#1f86cf" stroke-width="1.6"/><path d="M3.8 6.5 L6 8.8 L12 2.5" fill="none" stroke="#1f86cf" stroke-width="1.8"/></svg><span>Live monthly Q&amp;A event for all clients</span></li>
    <li><svg width="13" height="13" viewBox="0 0 13 13"><circle cx="6.5" cy="6.5" r="5.2" fill="none" stroke="#1f86cf" stroke-width="1.6"/><path d="M3.8 6.5 L6 8.8 L12 2.5" fill="none" stroke="#1f86cf" stroke-width="1.8"/></svg><span>Private peer-support group</span></li>
  </ul>

  <section class="advice">
    <h2 class="tab" style="top:9px;width:324px;padding-left:37px">EXPERT INSIDER ADVICE ON:</h2>
    <ul class="list advice-list" style="left:41px;top:57px;width:320px">
      <li><svg width="13" height="13" viewBox="0 0 13 13"><circle cx="6.5" cy="6.5" r="5.2" fill="none" stroke="#fff" stroke-width="1.6"/><path d="M3.8 6.5 L6 8.8 L12 2.5" fill="none" stroke="#fff" stroke-width="1.8"/></svg>Should you become a consultant?</li>
      <li><svg width="13" height="13" viewBox="0 0 13 13"><circle cx="6.5" cy="6.5" r="5.2" fill="none" stroke="#fff" stroke-width="1.6"/><path d="M3.8 6.5 L6 8.8 L12 2.5" fill="none" stroke="#fff" stroke-width="1.8"/></svg>Consulting CVs</li>
      <li><svg width="13" height="13" viewBox="0 0 13 13"><circle cx="6.5" cy="6.5" r="5.2" fill="none" stroke="#fff" stroke-width="1.6"/><path d="M3.8 6.5 L6 8.8 L12 2.5" fill="none" stroke="#fff" stroke-width="1.8"/></svg>Consulting Covering Letters</li>
      <li><svg width="13" height="13" viewBox="0 0 13 13"><circle cx="6.5" cy="6.5" r="5.2" fill="none" stroke="#fff" stroke-width="1.6"/><path d="M3.8 6.5 L6 8.8 L12 2.5" fill="none" stroke="#fff" stroke-width="1.8"/></svg>Case Interviews</li>
      <li><svg width="13" height="13" viewBox="0 0 13 13"><circle cx="6.5" cy="6.5" r="5.2" fill="none" stroke="#fff" stroke-width="1.6"/><path d="M3.8 6.5 L6 8.8 L12 2.5" fill="none" stroke="#fff" stroke-width="1.8"/></svg>Soft Skills&amp; Competences</li>
      <li><svg width="13" height="13" viewBox="0 0 13 13"><circle cx="6.5" cy="6.5" r="5.2" fill="none" stroke="#fff" stroke-width="1.6"/><path d="M3.8 6.5 L6 8.8 L12 2.5" fill="none" stroke="#fff" stroke-width="1.8"/></svg>Group interviews</li>
      <li><svg width="13" height="13" viewBox="0 0 13 13"><circle cx="6.5" cy="6.5" r="5.2" fill="none" stroke="#fff" stroke-width="1.6"/><path d="M3.8 6.5 L6 8.8 L12 2.5" fill="none" stroke="#fff" stroke-width="1.8"/></svg>Best firms &amp; countries to work in</li>
      <li><svg width="13" height="13" viewBox="0 0 13 13"><circle cx="6.5" cy="6.5" r="5.2" fill="none" stroke="#fff" stroke-width="1.6"/><path d="M3.8 6.5 L6 8.8 L12 2.5" fill="none" stroke="#fff" stroke-width="1.8"/></svg>The ‘up or out’ policy</li>
    </ul>
    <ul class="list advice-list" style="left:495px;top:57px;width:220px">
      <li><svg width="13" height="13" viewBox="0 0 13 13"><circle cx="6.5" cy="6.5" r="5.2" fill="none" stroke="#fff" stroke-width="1.6"/><path d="M3.8 6.5 L6 8.8 L12 2.5" fill="none" stroke="#fff" stroke-width="1.8"/></svg>A day in the life of a consultant</li>
      <li><svg width="13" height="13" viewBox="0 0 13 13"><circle cx="6.5" cy="6.5" r="5.2" fill="none" stroke="#fff" stroke-width="1.6"/><path d="M3.8 6.5 L6 8.8 L12 2.5" fill="none" stroke="#fff" stroke-width="1.8"/></svg>Consulting interviews</li>
      <li><svg width="13" height="13" viewBox="0 0 13 13"><circle cx="6.5" cy="6.5" r="5.2" fill="none" stroke="#fff" stroke-width="1.6"/><path d="M3.8 6.5 L6 8.8 L12 2.5" fill="none" stroke="#fff" stroke-width="1.8"/></svg>Partner Interviews</li>
      <li><svg width="13" height="13" viewBox="0 0 13 13"><circle cx="6.5" cy="6.5" r="5.2" fill="none" stroke="#fff" stroke-width="1.6"/><path d="M3.8 6.5 L6 8.8 L12 2.5" fill="none" stroke="#fff" stroke-width="1.8"/></svg>Estimation interviews</li>
      <li><svg width="13" height="13" viewBox="0 0 13 13"><circle cx="6.5" cy="6.5" r="5.2" fill="none" stroke="#fff" stroke-width="1.6"/><path d="M3.8 6.5 L6 8.8 L12 2.5" fill="none" stroke="#fff" stroke-width="1.8"/></svg>Psychometrics</li>
      <li><svg width="13" height="13" viewBox="0 0 13 13"><circle cx="6.5" cy="6.5" r="5.2" fill="none" stroke="#fff" stroke-width="1.6"/><path d="M3.8 6.5 L6 8.8 L12 2.5" fill="none" stroke="#fff" stroke-width="1.8"/></svg>Online assessments</li>
      <li><svg width="13" height="13" viewBox="0 0 13 13"><circle cx="6.5" cy="6.5" r="5.2" fill="none" stroke="#fff" stroke-width="1.6"/><path d="M3.8 6.5 L6 8.8 L12 2.5" fill="none" stroke="#fff" stroke-width="1.8"/></svg>How to progress</li>
      <li><svg width="13" height="13" viewBox="0 0 13 13"><circle cx="6.5" cy="6.5" r="5.2" fill="none" stroke="#fff" stroke-width="1.6"/><path d="M3.8 6.5 L6 8.8 L12 2.5" fill="none" stroke="#fff" stroke-width="1.8"/></svg>Networking for success</li>
    </ul>
  </section>

  <svg class="portrait" viewBox="0 0 258 440" role="img" aria-label="Portrait photo of Prof. Max Whitford in a beige blazer, arms crossed">
    <defs>
      <linearGradient id="portraitFill" x1="0" y1="0" x2="0" y2="1">
        <stop offset="0" stop-color="#b89a86"/>
        <stop offset=".35" stop-color="#c9bcab"/>
        <stop offset="1" stop-color="#a89a88"/>
      </linearGradient>
    </defs>
    <path d="M120 0 Q155 0 160 40 L160 100 Q230 120 258 150 V440 H8 Q14 300 20 250 Q30 150 85 115 L82 40 Q86 0 120 0 Z" fill="url(#portraitFill)"/>
  </svg>

  <h2 class="tab" style="top:797px;width:285px;padding-left:41px">PROF. MAX WHITFORD:</h2>
  <p class="bio">Is an ex-consultant&amp; recruiter who has helped over 700 students land consulting jobs. He has worked with or for all the major consultancies and wrote the world’s best-selling textbook on consultancy. His courses on consultancy have won national and international awards.</p>

  <h2 class="tab" style="top:957px;width:158px;padding-left:41px">PRICING</h2>
  <div class="price" style="left:92px"><span class="price-label" style="top:23px">100 licences:</span><span class="price-ribbon">£2500</span></div>
  <div class="price" style="left:238px"><span class="price-label" style="top:25px">1000 licences:</span><span class="price-ribbon">£4000</span></div>
  <div class="price" style="left:386px"><span class="price-label" style="top:22px">500 licences:</span><span class="price-ribbon">£3500</span></div>
  <div class="price" style="left:543px"><span class="price-label" style="top:9px">Unlimited<br>licences:</span><span class="price-ribbon">£4500</span></div>

  <footer class="footer">www.advisorysummit.example<span class="footer-sep">|</span>max@advisorysummit.example</footer>
</main>
</body>
</html>
```